Parcel Haven
Website design - Gifts and Occasions
Website design
Gifts and Occasions
The company is a gift giving service that helps people pick out the perfect gift based on an algorthim
above header
https://www.pallorby.net/
BrightMarkup BrightMarkup

```html
<!DOCTYPE html>
<html lang="en">
<head>
<meta charset="utf-8">
<title>Parcel Haven</title>
<link rel="stylesheet" href="https://fonts.googleapis.com/css2?family=Open+Sans:wght@400;600;700&family=Roboto:wght@500&display=swap">
<style>
  :root {
    --header-top: #8fcdd1;
    --header-bottom: #b3e0e2;
    --page-bg: #f3fafa;
    --page-bg-end: #fbfdfd;
    --brown: #7a4a0d;
    --brown-dark: #5e3807;
    --text: #2b2b2b;
    --label: #ffffff;
    --teal-text: #7cc5cb;
    --rule: #e2eeee;
  }
  * { box-sizing: border-box; margin: 0; padding: 0; }
  html, body { width: 1200px; height: 586px; overflow: hidden; }
  body {
    position: relative;
    font-family: "Open Sans", Arial, sans-serif;
    background: linear-gradient(180deg, var(--page-bg), var(--page-bg-end));
    color: var(--text);
  }
  .site-header {
    position: absolute; left: 0; top: 0; width: 1200px; height: 113px;
    background: linear-gradient(180deg, var(--header-top), var(--header-bottom));
  }
  .brand-tile {
    position: absolute; left: 139px; top: 10px; width: 96px; height: 96px;
    background: #fff; display: flex; align-items: center; justify-content: center;
  }
  .brand-tile .brand-name {
    font-size: 13px; font-weight: 600; color: var(--brown);
  }
  .login-form { position: absolute; left: 461px; top: 24px; }
  .field { position: absolute; top: 0; }
  .field label { display: block; font-size: 13px; color: var(--label); height: 19px; }
  .field input {
    width: 187px; height: 34px; border: 1px solid #d7eaeb; background: #fff;
  }
  .field-user { left: 0; }
  .field-pass { left: 194px; }
  .btn {
    position: absolute; top: 19px; height: 36px;
    background: var(--brown); color: #fff; border: none;
    border-bottom: 2px solid var(--brown-dark);
    font-family: "Roboto", Arial, sans-serif; font-weight: 500; font-size: 15px;
  }
  .btn-login { left: 391px; width: 72px; }
  .btn-signup { left: 506px; width: 91px; }
  .or { position: absolute; left: 476px; top: 27px; font-size: 14px; color: #fff; }

  .about { position: absolute; left: 142px; top: 168px; width: 520px; }
  .about h1 { font-size: 31px; font-weight: 700; color: var(--brown); margin-bottom: 2px; }
  .about p { font-size: 12.5px; line-height: 29px; }
  .about p + p { margin-top: 2px; }

  .feature-brand {
    position: absolute; left: 773px; top: 282px; width: 259px;
    text-align: center; font-size: 34px; font-weight: 600; color: var(--brown);
  }

  .site-footer {
    position: absolute; left: 0; top: 504px; width: 1200px; height: 82px;
    background: #fff; border-top: 1px solid var(--rule);
    padding: 16px 0 0 142px; font-size: 12.5px; color: var(--teal-text); line-height: 29px;
  }
</style>
</head>
<body>
  <header class="site-header">
    <div class="brand-tile">
      <span class="brand-name">Parcel Haven</span>
    </div>
    <form class="login-form">
      <div class="field field-user"><label>User Name</label><input type="text"></div>
      <div class="field field-pass"><label>Password</label><input type="password"></div>
      <button class="btn btn-login" type="button">Log in</button>
      <span class="or">or</span>
      <button class="btn btn-signup" type="button">SIGN UP</button>
    </form>
  </header>

  <main>
    <section class="about">
      <h1>About Us</h1>
      <p>Parcel Haven is a gift giving service that recommends the best gift for your personal or professional relationship. We will organize your upcoming events and notify you if a gift may need to be sent.</p>
      <p>Parcel Haven utilizes complex computer algorithms to recommend you a gift.</p>
    </section>
    <div class="feature-brand">Parcel Haven</div>
  </main>

  <footer class="site-footer">
    <div>Parcel Haven © 2014</div>
    <div>English (US)</div>
  </footer>
</body>
</html>
```